Private Dining Restaurant Menu Design

Looking for help in designing a private dining room menu brochure - probably would need 4 panel layout to make all of the content fit, or a 5.5x8" booklet. Open to your ideas on layout/vessel - would want to post on website and be able to print to hand out to guests interested in booking our private dining room.

All content is in the attached "Private Dining Menu".

Would like to match existing dinner menu design - also attached.

Website is www.tallowfenkitchen.com

Requirements
Must have
• Easy to read format of a brochure of the private dining menu content - want to be able to hand out to interested guests and have it simple and easy to read/flip through.

```html
<!DOCTYPE html>
<html lang="en">
<head>
<meta charset="utf-8">
<title>Sandwiches, Tacos, Salads &amp; Soups Menu</title>
<link href="https://fonts.googleapis.com/css2?family=Tinos:wght@700&family=Roboto+Condensed:wght@400;500&family=Open+Sans:ital@1&display=swap" rel="stylesheet">
<style>
  :root {
    --bg: #28272e;
    --gold: #ecc96c;
    --gold-dark: #a8802c;
    --gold-light: #e7c877;
    --text: #ffffff;
  }
  * { margin: 0; padding: 0; box-sizing: border-box; }
  html, body { width: 849px; height: 1200px; overflow: hidden; background: var(--bg); }
  .menu-page {
    position: relative; width: 849px; height: 1200px; background: var(--bg);
    color: var(--text); font-family: "Roboto Condensed", "Arial Narrow", sans-serif;
  }
  .frame { position: absolute; inset: 0; }
  .section { position: absolute; left: 45px; right: 30px; }
  .section-title {
    font-family: "Tinos", "Times New Roman", serif; font-weight: 700;
    font-size: 37px; line-height: 1; white-space: nowrap;
    background: linear-gradient(180deg, var(--gold-light) 10%, var(--gold-dark) 95%);
    -webkit-background-clip: text; background-clip: text; color: transparent;
  }
  .section-note { font-family: "Open Sans", Verdana, sans-serif; font-style: italic; }
  .price { font-family: "Open Sans", Verdana, sans-serif; font-style: italic; }

  .sandwiches { top: 92px; }
  .sandwiches .section-note { font-size: 14px; line-height: 15.5px; margin-top: 14px; }
  .sandwiches .dish-list { margin-top: 14px; }
  .sandwiches .dish { height: 44.3px; }
  .sandwiches .dish-name { font-size: 16px; font-weight: 500; line-height: 18px; }
  .sandwiches .dish-desc { font-size: 11px; line-height: 18px; white-space: nowrap; }
  .sandwiches .dish-desc .price { font-size: 12px; }
  .sandwiches .dish.featured .dish-desc { font-size: 15px; line-height: 22px; }
  .sandwiches .dish.featured .dish-desc .price { font-size: 12.5px; }

  .salads { top: 603px; }
  .salads .section-note { font-size: 12.2px; margin-top: 23px; line-height: 15px; }
  .salads .dish-list { margin-top: 11px; }
  .salads .dish { min-height: 36px; }
  .salads .dish.wrap { min-height: 50px; }
  .salads .dish-name { font-size: 13.6px; font-weight: 500; line-height: 15px; }
  .salads .dish-desc { font-size: 10.1px; line-height: 14.5px; }
  .salads .dish-desc .price { font-size: 11px; }
  .soup-name { font-size: 13.6px; font-weight: 500; line-height: 15px; }
  .soup-name .size { font-size: 10.5px; }
  .soup-list { list-style: none; display: flex; gap: 20px; font-size: 10px; margin-left: 7px; line-height: 15px; }
  .soup-list li + li::before { content: "• "; }
</style>
</head>
<body>
<main class="menu-page">
  <svg class="frame" width="849" height="1200" viewBox="0 0 849 1200" aria-hidden="true">
    <g fill="none" stroke="var(--gold)" stroke-width="2.5">
      <path d="M40 10 H802 A30 30 0 0 0 832 40 V1158 A30 30 0 0 0 802 1188 H40 A30 30 0 0 0 10 1158 V40 A30 30 0 0 0 40 10 Z"/>
    </g>
    <g fill="none" stroke="var(--gold)" stroke-width="1.2" opacity="0.9">
      <path d="M110 22 H806 A24 24 0 0 0 828 46 V1140"/>
      <path d="M820 30 V1170 A22 22 0 0 0 798 1180 H40"/>
      <path d="M22 120 V1150 A24 24 0 0 1 44 1174"/>
    </g>
  </svg>

  <section class="section sandwiches">
    <h1 class="section-title">SANDWICHES and TACOS</h1>
    <p class="section-note">All sandwiches come with your choice of fries, cheesy hash browns, soup or creamy coleslaw.<br>Upgrade to potato skins, fresh fruit or sweet potato fries. 2</p>
    <div class="dish-list">
      <div class="dish"><h2 class="dish-name">CHICAGO STEAK SANDWICH</h2><p class="dish-desc">Ribeye shaved thin &amp; grilled with giardanera &amp; cheese sauce. Served with au jus for dipping. <span class="price">15</span></p></div>
      <div class="dish"><h2 class="dish-name">CHICKEN TACOS</h2><p class="dish-desc">Grilled tacos filled with rotisserie chicken, black beans, roasted corn salsa, pico, lettuce &amp; chipotle ranch. <span class="price">11</span></p></div>
      <div class="dish"><h2 class="dish-name">WALLEYE TACOS</h2><p class="dish-desc">Your choice of Blackened or Northwoods Breaded walleye with green cabbage, mozzarella, lemon aioli &amp; pico de gallo. <span class="price">13</span></p></div>
      <div class="dish"><h2 class="dish-name">HOUSE SMOKED BBQ PORK</h2><p class="dish-desc">Topped with creamy cole slaw on a buttered bun. <span class="price">10</span></p></div>
      <div class="dish"><h2 class="dish-name">AVOCADO BACON ROTISSERIE</h2><p class="dish-desc">Chicken, avocado, thick-cut bacon, provolone, ranch dressing, tomato &amp; spring mix. <span class="price">13</span></p></div>
      <div class="dish"><h2 class="dish-name">PEPPER JACK TURKEY MELT</h2><p class="dish-desc">Thick-cut bacon, lettuce, vine ripened tomato &amp; spicy mayo on a pretzel bun. <span class="price">13</span></p></div>
      <div class="dish"><h2 class="dish-name">WALLEYE SANDWICH</h2><p class="dish-desc">Lemon herb aioli, field greens, tomatoes &amp; pickles. <span class="price">14</span></p></div>
      <div class="dish featured"><h2 class="dish-name">SOUTHWEST SPICED-CHICKEN SANDWICH</h2><p class="dish-desc">Seasoned wood-roasted chicken, peppers, pickled jalapeños, onions, pepper jack cheese &amp; spicy mayo on ciabatta bread. <span class="price">11</span></p></div>
    </div>
  </section>

  <section class="section salads">
    <h1 class="section-title">SALADS &amp; SOUPS</h1>
    <p class="section-note">Add to any salad: rotisserie chicken 4 or fresh salmon 7</p>
    <div class="dish-list">
      <div class="dish"><h2 class="dish-name">STARTER HOUSE SALAD</h2><p class="dish-desc">Mixed greens, craisins, pepitas, goat cheese with blood orange vinaigrette. <span class="price">5</span></p></div>
      <div class="dish"><h2 class="dish-name">STARTER WEDGE SALAD</h2><p class="dish-desc">Iceberg lettuce, thick-cut bacon, cherry tomatoes, fresh herbs with bleu cheese dressing. <span class="price">5</span></p></div>
      <div class="dish wrap"><h2 class="dish-name">APPLEWOOD BACON &amp; FAJITA CHICKEN SALAD</h2><p class="dish-desc">Fajita seasoned rotisserie chicken, fresh peppers, onions &amp; roasted corn on top of crisp romaine with smoked bacon, cheddar jack cheeses, tomatoes, black beans &amp; chipotle ranch dressing. <span class="price">13</span></p></div>
      <div class="dish"><h2 class="dish-name">ROTISSERIE CHICKEN SALAD</h2><p class="dish-desc">Fresh romaine, wood-roasted chicken, tomatoes, bacon, cucumbers, cheddar &amp; jack cheeses, carrots, toasted pecans &amp; creamy house ranch dressing. <span class="price">13</span></p></div>
      <div class="dish"><h2 class="dish-name">PERFECT SUMMER SALAD</h2><p class="dish-desc">Fresh romaine, fresh strawberries, fresh raspberries, pineapple, mango, red onion &amp; pecans served with house poppy seed dressing. <span class="price">11</span></p></div>
      <div class="dish"><h2 class="dish-name">COCONUT SHRIMP &amp; TROPICAL FRUIT SALAD</h2><p class="dish-desc">Mixed greens with fresh mango, pineapple, raspberries, almonds, feta cheese &amp; coconut shrimp topped with our house made Parmesan vanilla dressing. <span class="price">15</span></p></div>
      <div class="dish wrap"><h2 class="dish-name">HOLLIS’S CHOPPED SALAD</h2><p class="dish-desc">Wood-roasted chicken, mixed greens, bleu cheese crumbles, vine-ripened tomato, avocado, charred corn, thick-cut bacon, green onion &amp; corn tortilla strips tossed in our house made honey-lime vinaigrette. <span class="price">14</span></p></div>
      <div class="dish soups">
        <h2 class="soup-name">HOMEMADE SOUPS <span class="size">Cup</span> <span class="price size">4</span> <span class="size">Bowl</span> <span class="price size">7</span></h2>
        <ul class="soup-list"><li>CHICKEN WILD RICE SOUP</li><li>WHITE CHICKEN CHILI</li><li>SOUP OF THE DAY</li></ul>
      </div>
    </div>
  </section>
</main>
</body>
</html>
```